I am looking for a designer for my Gratitude Journal cover design. This is a daily gratitude journal designed for women. The interior features colored pages with a daily gratitude section, weekly habit tracker, and monthly reflection. The journal has enough space for a 12-week journaling.
Book size: 6x 9 inches
Paperback Print Book
Page count: 117
Platform: Nimbo BPX
Book title: I’m Unfinished, Who Cares?
Design Style:
-Boho style color and graphics, color choice is free but must follow color psychology, no pure black. The color and styling should correlate to the interior pages (In the attachment).
-There could be a female silhouette on the front cover, but not as big as the whole cover. (doesn’t have to if not looking good)
-No text or interior page preview on the back cover. Only pen name logo on the bottom middle of the back cover and make it small and subtle. (Pen name logo attached)
-Book title on front cover and spine, author name only on spine (Author name: Tobias Wexley).
-No other text on the front cover.
All design elements including fonts must be commercially licensed, and you must provide source files and commercial licenses of them together as part of the delivery.
nimbo.example

```html
<!DOCTYPE html>
<html lang="en">
<head>
<meta charset="utf-8">
<title>I’m Unfinished, Who Cares? — Cover</title>
<link rel="stylesheet" href="https://fonts.googleapis.com/css2?family=Kalam:wght@700&family=Montserrat:wght@600&display=swap">
<style>
  :root {
    --page-bg: #ffffff;
    --cover-sand: #ecdcd0;
    --cover-sand-light: #f3e7dd;
    --wreath-blush: #e2ae9c;
    --wreath-terracotta: #c9755c;
    --wreath-amber: #e3a565;
    --wreath-sage: #c9cbb6;
    --title-brown: #7b3428;
    --subtitle-brown: #5b2c22;
    --author-tan: #c98a66;
  }
  * { margin: 0; padding: 0; box-sizing: border-box; }
  html, body {
    width: 1200px;
    height: 1200px;
    overflow: hidden;
    background: var(--page-bg);
  }
  .canvas {
    position: relative;
    width: 1200px;
    height: 1200px;
  }
  .cover {
    position: absolute;
    left: 233px;
    top: 50px;
    width: 734px;
    height: 1100px;
    overflow: hidden;
    background: linear-gradient(160deg, var(--cover-sand-light) 0%, var(--cover-sand) 60%, #e8d6c8 100%);
  }
  .cover-artwork {
    position: absolute;
    inset: 0;
    width: 100%;
    height: 100%;
  }
  .title {
    position: absolute;
    left: 20px;
    right: 0;
    top: 338px;
    text-align: center;
    font-family: "Kalam", cursive;
    font-weight: 700;
    font-size: 90px;
    line-height: 94px;
    color: var(--title-brown);
  }
  .subtitle {
    position: absolute;
    left: 20px;
    right: 0;
    top: 644px;
    text-align: center;
    font-family: "Montserrat", sans-serif;
    font-weight: 600;
    font-size: 17px;
    letter-spacing: 1.2px;
    color: var(--subtitle-brown);
  }
  .author {
    position: absolute;
    left: 0;
    right: 0;
    top: 1018px;
    text-align: center;
    font-family: "Montserrat", sans-serif;
    font-weight: 600;
    font-size: 29px;
    letter-spacing: 1.5px;
    color: var(--author-tan);
  }
</style>
</head>
<body>
<main class="canvas">
  <section class="cover">
    <svg class="cover-artwork" viewBox="0 0 734 1100" role="img" aria-label="Boho watercolor floral wreath in blush, terracotta, amber and sage around a pale circle, with a small sketched woman in a flowing dress at its base">
      <defs>
        <radialGradient id="wreath-tones" cx="50%" cy="50%" r="50%">
          <stop offset="0%" stop-color="var(--cover-sand-light)"/>
          <stop offset="58%" stop-color="var(--cover-sand-light)"/>
          <stop offset="70%" stop-color="var(--wreath-blush)"/>
          <stop offset="82%" stop-color="var(--wreath-terracotta)" stop-opacity="0.75"/>
          <stop offset="92%" stop-color="var(--wreath-amber)" stop-opacity="0.45"/>
          <stop offset="100%" stop-color="var(--cover-sand)" stop-opacity="0"/>
        </radialGradient>
      </defs>
      <ellipse cx="384" cy="510" rx="400" ry="380" fill="url(#wreath-tones)"/>
      <circle cx="384" cy="500" r="232" fill="var(--cover-sand-light)" opacity="0.9"/>
    </svg>
    <h1 class="title">I’m<br>Unfinished,<br>Who Cares?</h1>
    <p class="subtitle">DAILY GRATITUDE JOURNAL</p>
    <p class="author">TOBIAS WEXLEY</p>
  </section>
</main>
</body>
</html>
```